Brindle Wealth Management Flow Charts

I need help creating three flow charts for my businesses website. We want them to be simple but look professional. This is for a Wealth Management firm. I will attach a word document that has all of the descriptions for everything so you know what icons to use. We just want the chart to have an icon, the names of each step and the corresponding numbers. I will also include some examples of charts we liked as well. Once the winner is selected, we will need help with additional graphic design elements for our website ASAP.
Other font styles liked:
- Goudy Roman

```html
<!DOCTYPE html>
<html lang="en">
<head>
<meta charset="UTF-8">
<title>6 Steps for the Retirement Planning Process</title>
<link rel="stylesheet" href="https://fonts.googleapis.com/css2?family=Roboto+Slab:wght@200;300;400;700&display=swap">
<style>
  :root {
    --bg: #ffffff;
    --step-discovery: #2bb0e0;
    --step-learning: #093c5e;
    --step-planning: #e4525f;
    --step-execution: #f8c516;
    --step-alignment: #f39333;
    --step-review: #86c66f;
    --hub-light: #f4f5f6;
    --hub-dark: #cfd2d6;
    --hub-text: #2e3a4a;
    --accent: #f39333;
    --hanger: #2f3540;
    --label: #ffffff;
  }
  * { margin: 0; padding: 0; box-sizing: border-box; }
  html, body {
    width: 1200px; height: 1200px; overflow: hidden;
    background: var(--bg);
  }
  .canvas {
    position: relative; width: 1200px; height: 1200px;
    font-family: "Roboto Slab", Georgia, serif;
  }
  .wheel { position: absolute; inset: 0; }
  .step {
    position: absolute; transform: translateX(-50%);
    display: flex; flex-direction: column; align-items: center;
    color: var(--label); text-align: center; white-space: nowrap;
  }
  .step__number {
    font-weight: 200; font-size: 74px; line-height: 1; letter-spacing: 2px;
  }
  .step__icon { width: 60px; height: 60px; margin: 18px 0 12px; }
  .step__name {
    font-weight: 400; font-size: 31px; line-height: 1.2; text-transform: uppercase;
  }
  .hub-text {
    position: absolute; left: 614px; top: 612px; transform: translate(-50%, -50%);
    width: 240px; text-align: center; color: var(--hub-text);
    text-transform: uppercase; font-weight: 700; font-size: 20px; line-height: 36px;
  }
  .hub-text__count {
    display: block; color: var(--accent); font-size: 58px; line-height: 1; margin-bottom: 8px;
  }
</style>
</head>
<body>
<div class="canvas">
  <svg class="wheel" viewBox="0 0 1200 1200" width="1200" height="1200" aria-hidden="true">
    <defs>
      <radialGradient id="hubFill" cx="40%" cy="35%" r="70%">
        <stop offset="0%" stop-color="var(--hub-light)"/>
        <stop offset="100%" stop-color="var(--hub-dark)"/>
      </radialGradient>
      <filter id="hubShadow" x="-30%" y="-30%" width="160%" height="160%">
        <feDropShadow dx="0" dy="4" stdDeviation="8" flood-color="#000" flood-opacity="0.25"/>
      </filter>
    </defs>
    <path class="hanger" d="M584 106 Q584 62 614 62 Q644 62 644 106 Z" fill="var(--hanger)"/>
    <circle cx="614" cy="84" r="8" fill="#fff"/>
    <g stroke="#fff" stroke-width="12" stroke-linejoin="round">
      <path class="segment segment--discovery" d="M614 610 L364 174 A510 510 0 0 1 880 186 Z" fill="var(--step-discovery)"/>
      <path class="segment segment--learning" d="M614 610 L880 186 A510 510 0 0 1 1120 630 L950 670 Z" fill="var(--step-learning)"/>
      <path class="segment segment--planning" d="M614 610 L950 670 L1120 630 A510 510 0 0 1 860 1064 Z" fill="var(--step-planning)"/>
      <path class="segment segment--execution" d="M614 610 L860 1064 A510 510 0 0 1 350 1058 L380 880 Z" fill="var(--step-execution)"/>
      <path class="segment segment--alignment" d="M614 610 L380 880 L350 1058 A510 510 0 0 1 102 590 Z" fill="var(--step-alignment)"/>
      <path class="segment segment--review" d="M614 610 L102 590 A510 510 0 0 1 364 174 Z" fill="var(--step-review)"/>
    </g>
    <circle cx="614" cy="610" r="172" fill="#fff"/>
    <circle class="hub" cx="614" cy="610" r="150" fill="url(#hubFill)" filter="url(#hubShadow)"/>
  </svg>

  <div class="step step--discovery" style="left:636px; top:142px;">
    <div class="step__number">01</div>
    <svg class="step__icon" viewBox="0 0 64 64" fill="#fff" aria-hidden="true">
      <path d="M32 4a20 20 0 0 0-12 36c3 2.5 4 5 4 8h16c0-3 1-5.5 4-8A20 20 0 0 0 32 4z"/>
      <rect x="24" y="51" width="16" height="4" rx="2"/><rect x="26" y="57" width="12" height="4" rx="2"/>
      <path d="M32 42V26M26 22l6 6 6-6" stroke="var(--step-discovery)" stroke-width="3" fill="none"/>
    </svg>
    <div class="step__name">Discovery<br>Meeting</div>
  </div>

  <div class="step step--learning" style="left:940px; top:320px;">
    <div class="step__number">02</div>
    <svg class="step__icon" viewBox="0 0 64 64" fill="#fff" aria-hidden="true">
      <rect x="6" y="6" width="52" height="38" rx="2"/>
      <g fill="var(--step-learning)"><circle cx="16" cy="17" r="3"/><circle cx="16" cy="27" r="3"/><circle cx="16" cy="36" r="2.5"/>
      <rect x="24" y="15" width="26" height="4"/><rect x="24" y="25" width="26" height="4"/><rect x="24" y="34" width="20" height="4"/></g>
      <path d="M32 44v8M32 52l-10 9M32 52l10 9" stroke="#fff" stroke-width="3"/>
    </svg>
    <div class="step__name">Learning</div>
  </div>

  <div class="step step--planning" style="left:880px; top:700px;">
    <div class="step__number">03</div>
    <svg class="step__icon" viewBox="0 0 64 64" fill="#fff" aria-hidden="true">
      <rect x="8" y="6" width="18" height="12" rx="3"/><rect x="38" y="6" width="18" height="12" rx="3"/>
      <path d="M4 22h26v34a4 4 0 0 1-4 4H8a4 4 0 0 1-4-4z"/><path d="M34 22h26v34a4 4 0 0 1-4 4H38a4 4 0 0 1-4-4z"/>
      <rect x="26" y="26" width="12" height="14"/>
      <rect x="9" y="44" width="16" height="10" rx="2" fill="var(--step-planning)"/><rect x="39" y="44" width="16" height="10" rx="2" fill="var(--step-planning)"/>
    </svg>
    <div class="step__name">Planning</div>
  </div>

  <div class="step step--execution" style="left:576px; top:826px;">
    <div class="step__number">04</div>
    <svg class="step__icon" viewBox="0 0 64 64" fill="#fff" aria-hidden="true">
      <path d="M58 6C42 6 30 14 22 30l12 12c16-8 24-20 24-36z"/>
      <circle cx="42" cy="22" r="5" fill="var(--step-execution)"/>
      <path d="M22 30l-12 2 8-10h10zM34 42l-2 12 10-8V36z"/>
      <path d="M18 40c-6 2-10 8-10 16 8 0 14-4 16-10z"/>
    </svg>
    <div class="step__name">Execution</div>
  </div>

  <div class="step step--alignment" style="left:284px; top:604px;">
    <div class="step__number">05</div>
    <svg class="step__icon" viewBox="0 0 64 64" fill="#fff" aria-hidden="true">
      <rect x="6" y="56" width="52" height="4"/>
      <rect x="12" y="38" width="8" height="16"/><rect x="24" y="32" width="8" height="22"/><rect x="36" y="40" width="8" height="14"/><rect x="48" y="28" width="8" height="26"/>
      <path d="M8 30l14-14 10 8 18-16" stroke="#fff" stroke-width="4" fill="none"/>
      <path d="M44 6h12v12z"/>
    </svg>
    <div class="step__name">Alignment</div>
  </div>

  <div class="step step--review" style="left:316px; top:280px;">
    <div class="step__number">06</div>
    <svg class="step__icon" viewBox="0 0 64 64" fill="#fff" aria-hidden="true">
      <rect x="4" y="28" width="14" height="30" rx="2"/>
      <path d="M22 30l10-18c2-4 8-3 8 2v10h14a5 5 0 0 1 5 6l-4 22a5 5 0 0 1-5 4H22z"/>
    </svg>
    <div class="step__name">Review</div>
  </div>

  <div class="hub-text">
    <span class="hub-text__count">6</span>
    Steps for the<br>Retirement<br>Planning<br>Process
  </div>
</div>
</body>
</html>
```